Award Winning Production Company Needs Poster for Lastest Film

Nothing’s Amiss Pictures is looking for a movie poster for our short film "Refrain" to be used at film festivals. Refrain is a short film about a pair of StreamNook stars named Hazel and Juniper who write and perform songs together. Juniper is moving to a new city and Hazel comes to visit and see her new apartment. The film is shot in one shot as if it is livestream Juniper is hosting where she is giving Hazel and their followers a tour of the new living space. As the tour progresses Hazel begins to see that Juniper is starting to move on without her and tension builds between the two of them.

Along with a trailer, we’ve included some photos to potentially base your posters on but don't restrict yourself to just using them. You are free to use whatever elements you want! It is not required that you use the provided photos and we encourage creativity with other elements as well.

Target Market(s)

Film Festival Attendees, Milennials

Industry/Entity Type

Film Production

Requirements
Must have
• Please include these credits on the poster:
• Our company: Nothing’s Amiss Pictures
• Our stars names: Marisa Pellwright and Tamsin Kowalcek
• Directed by Dale and Brent Ushworth
• Story by Jem Ushworth
• Original Music by Marisa Pellwright
Nice to have
• We are currently debating amongst ourselves between two titles: “Refrain” and “Hazel Shows Juniper’s Fresh Loft!” You can submit posters using either title or both.

```html
<!DOCTYPE html>
<html lang="en">
<head>
<meta charset="utf-8">
<title>Refrain — Poster</title>
<link rel="stylesheet" href="https://fonts.googleapis.com/css2?family=Alfa+Slab+One&family=Oswald:wght@700&family=Libre+Baskerville&display=swap">
<style>
  :root {
    --ink: #000000;
    --paper: #ffffff;
    --rose: #b8325f;
    --rose-deep: #6e1634;
    --haze: #c9c4c6;
    --smoke: #8d8a8c;
    --frame: #9a9a9a;
  }
  html, body {
    margin: 0;
    padding: 0;
    width: 960px;
    height: 1200px;
    overflow: hidden;
    background: var(--ink);
  }
  .poster {
    position: relative;
    width: 960px;
    height: 1200px;
    background: var(--ink);
    box-shadow: inset 0 0 0 2px var(--frame);
    overflow: hidden;
  }
  .key-art {
    position: absolute;
    left: 76px;
    top: 84px;
    width: 792px;
    height: 928px;
    background:
      radial-gradient(ellipse 55% 30% at 65% 72%, rgba(235,232,234,0.95), rgba(235,232,234,0) 70%),
      radial-gradient(ellipse 40% 22% at 35% 62%, rgba(220,216,218,0.85), rgba(220,216,218,0) 70%),
      linear-gradient(180deg, var(--rose) 0%, var(--rose-deep) 45%, var(--smoke) 70%, var(--haze) 100%);
  }
  .overlay {
    position: absolute;
    left: 0;
    top: 0;
    width: 960px;
    height: 1200px;
  }
  .star-name {
    position: absolute;
    background: var(--ink);
    color: var(--paper);
    font-family: "Oswald", "Arial Narrow", sans-serif;
    font-weight: 700;
    font-size: 40px;
    line-height: 1;
    text-transform: uppercase;
    letter-spacing: 0.5px;
    text-shadow: 3px 3px 0 var(--rose);
    padding: 18px 20px 22px 8px;
    white-space: nowrap;
  }
  .star-one { left: 60px; top: 470px; width: 380px; transform: rotate(-2deg); }
  .star-two { left: 64px; top: 716px; width: 388px; transform: rotate(-2.5deg); padding-left: 12px; }
  .credits {
    position: absolute;
    left: 0;
    top: 1038px;
    width: 960px;
    text-align: center;
    color: var(--paper);
    font-family: "Libre Baskerville", Georgia, serif;
    text-transform: uppercase;
  }
  .company {
    font-size: 18px;
    letter-spacing: 4.5px;
    margin: 0 0 16px;
  }
  .credit-line {
    font-size: 13.5px;
    letter-spacing: 1px;
    margin: 0 0 8px;
  }
</style>
</head>
<body>
<main class="poster">
  <div class="key-art" role="img" aria-label="Close-up portrait of a singer bathed in pink light, with drifting white smoke and a guitar below"></div>

  <svg class="overlay" viewBox="0 0 960 1200" aria-hidden="true">
    <g class="stripes" fill="#000">
      <polygon points="76,84 226,84 194,1012 76,1012"/>
      <polygon points="278,84 328,84 318,1012 264,1012"/>
      <polygon points="500,84 612,84 612,708 500,708"/>
      <polygon points="684,84 728,84 718,530 678,530"/>
      <polygon points="800,84 840,84 840,540 778,512"/>
    </g>
    <g class="title" font-family="'Alfa Slab One', serif" font-size="112">
      <text transform="translate(560 684) rotate(-90)" textLength="520" lengthAdjust="spacingAndGlyphs"
            x="0" y="38" fill="#7a7a7a">REFRAIN</text>
      <text transform="translate(556 680) rotate(-90)" textLength="520" lengthAdjust="spacingAndGlyphs"
            x="0" y="38" fill="#fff" stroke="#000" stroke-width="3" paint-order="stroke">REFRAIN</text>
    </g>
  </svg>

  <div class="star-name star-one">Marisa Pellwright</div>
  <div class="star-name star-two">Tamsin Kowalcek</div>

  <section class="credits">
    <p class="company">Nothing’s Amiss Pictures</p>
    <p class="credit-line">Directed by Dale and Brent Ushworth</p>
    <p class="credit-line">Story by Jem Ushworth</p>
    <p class="credit-line">Original Music by Marisa Pellwright</p>
  </section>
</main>
</body>
</html>
```